lantern productions business cards design

design a clean look but creative business card for a production company, I'm a freelance producer and launching my startup, would like to keep a clean professional look but still creative

Target Market(s)

businesses

Industry/Entity Type

video production

Contact Information for Business Card

logo, name (Mark Ellis), Title (Producer), (MFA Filmmaking, CSPT Los Angeles), contact number & email ID

Colors

Designer to choose only greyscale colors for use in the design.

Requirements
Must have
• logo, black and white colors, you can play with their shades
Nice to have
• a unique design, not necessarily a typical size card
Should not have
• too colorful or playful

```html
<!DOCTYPE html>
<html lang="en">
<head>
<meta charset="utf-8">
<title>Lantern Productions – Business Cards</title>
<link rel="stylesheet" href="https://fonts.googleapis.com/css2?family=Figtree:wght@400;600;700&display=swap">
<style>
  :root {
    --backdrop: #b4b4b4;
    --front-paper: #ffffff;
    --back-paper: #efeef2;
    --ink-dark: #2f2e30;
    --ink-mid: #6e6d70;
    --rule: #acabae;
    --band-grey: #8a8a8d;
    --band-grey-light: #b9b9bc;
  }
  * { margin: 0; padding: 0; box-sizing: border-box; }
  html, body {
    width: 1200px; height: 900px; overflow: hidden;
    background: var(--backdrop);
    font-family: "Figtree", sans-serif;
  }
  .card {
    position: absolute;
    left: 363px;
    width: 475px;
    height: 271px;
    overflow: hidden;
  }
  .card--front { top: 145px; background: var(--front-paper); }
  .card--back { top: 484px; background: var(--back-paper); }

  .front-wordmark {
    position: absolute; left: 0; right: 0; top: 262px;
    text-align: center;
    font-size: 30px; font-weight: 700; letter-spacing: 0.5px;
    color: var(--ink-dark);
  }
  .card--front .front-wordmark { top: 116px; }
  .front-url {
    position: absolute; left: 0; right: 0; top: 222px;
    text-align: center;
    font-size: 10.5px; letter-spacing: 0.6px;
    color: var(--ink-mid);
  }
  .front-url strong { font-weight: 700; }

  .holder {
    position: absolute; left: 44px; top: 47px;
    color: var(--ink-mid);
    font-size: 11px; line-height: 13.5px;
  }
  .holder-name {
    font-size: 16px; font-weight: 700; line-height: 20px;
    color: var(--ink-dark);
  }
  .back-wordmark {
    position: absolute; right: 52px; top: 70px;
    font-size: 15px; font-weight: 700;
    color: var(--ink-dark);
  }
  .divider {
    position: absolute; left: 44px; top: 160px;
    width: 379px; height: 1px; background: var(--rule);
  }
  .contact {
    position: absolute; left: 44px; top: 178px;
    font-size: 11px; line-height: 14px; color: var(--ink-mid);
    list-style: none;
  }
  .contact li { display: flex; align-items: center; gap: 7px; }
  .contact svg { width: 9px; height: 9px; fill: var(--ink-dark); }
  .back-url {
    position: absolute; right: 44px; top: 192px;
    font-size: 11px; line-height: 14px; color: var(--ink-mid);
  }
  .swoosh { position: absolute; left: 0; bottom: 0; width: 475px; height: 271px; }
</style>
</head>
<body>

<section class="card card--front">
  <div class="front-wordmark">lantern productions</div>
  <div class="front-url">www.<strong>lanternproductions</strong>.com</div>
</section>

<section class="card card--back">
  <svg class="swoosh" viewBox="0 0 475 271" aria-hidden="true">
    <defs>
      <linearGradient id="bandFade" x1="0" y1="0" x2="1" y2="0">
        <stop offset="0" stop-color="var(--band-grey)"/>
        <stop offset="1" stop-color="var(--band-grey-light)"/>
      </linearGradient>
    </defs>
    <path d="M0,271 L0,252 C110,237 230,229 350,227 L475,229 L475,271 Z" fill="url(#bandFade)"/>
    <path d="M72,271 C108,244 240,232 352,229 L475,230 L475,271 Z" fill="#ffffff"/>
    <path d="M78,271 C114,246 246,234 356,231 L475,232 L475,271 Z" fill="var(--ink-dark)"/>
  </svg>

  <div class="holder">
    <div class="holder-name">Mark Ellis</div>
    <div>Producer</div>
    <div>MFA in Filmmaking</div>
    <div>CSPT, Los Angeles</div>
  </div>

  <div class="back-wordmark">lantern productions</div>

  <div class="divider"></div>

  <ul class="contact">
    <li>
      <svg viewBox="0 0 10 10" aria-hidden="true"><path d="M2.2,0.6 L3.6,2.6 L2.7,3.6 C3.3,4.9 4.8,6.5 6.3,7.2 L7.3,6.3 L9.4,7.7 L8.5,9.4 C4.6,9.3 0.7,5.4 0.6,1.5 Z"/></svg>
      555.014.2290
    </li>
    <li>
      <svg viewBox="0 0 10 10" aria-hidden="true"><path d="M0.5,2 L9.5,2 L5,5.6 Z M0.5,3 L5,6.6 L9.5,3 L9.5,8.2 L0.5,8.2 Z"/></svg>
      markellis@lanternproductions.com
    </li>
  </ul>

  <div class="back-url">www.lanternproductions.com</div>
</section>

</body>
</html>
```